independent cleaner, reliable, custom, thorough, trustworthy

Not sure yet if I want single-sided or double sided, so I'm selecting double-sided just in case, but single-sided designs are okay.

Really looking to find the happy medium between personal and professional in a business card design. I end up building comfortable relationships with the people I work for.

Most of my business is through referrals, but I want some business cards to hand out to people who ask for one (and maybe put them on community bulletin boards).

My target market is homeowners and business owners who are looking for a reliable cleaner and are willing to pay a bit more to have excellent quality and someone they trust.

Theme: I have a personal-professional feel since I'm solo, so the theme should reflect that. Trustworthy, personal, simple. I clean up messes.

Hopefully this is enough info, let me know if you have any questions though of course!

Target Market(s)

Homeowners businessowners who are looking for a reliable cleaner, excellent quality trustworthy.

Industry/Entity Type

Cleaning Service

Contact Information for Business Card

Please include this text:
• Delphine Warrow
• independent cleaner
• reliable, custom, thorough
• 604-317-2269
• mtb.warrow@postmail.example

Font styles to use
Serif
Sans Serif

Colors
ffffff
00a990
0492cd
33a6d7
0355a3
3276b5
919191

Requirements
Must have
• Really looking to find the happy medium between personal and professional in a business card design.
• Background: at least 50% white on the side with the most text (coloured accents or shapes are okay)
• I lean more towards simple and clean, solid colours, maybe a gentle gradient
Nice to have
• Not sure yet if I want single-sided or double sided, so I'm selecting double-sided just in case, but single-sided designs are okay.
• Colours: preferably blues and teals for the font and other objects (if any). Open to designer's choice though. I've toyed around with orangey-yellow, but it doesn't feel right and I keep going back to blues/teals
• Also I uploaded a sketch of my signature and initials so you can get a feel for my personality. I'm not expecting this to be included in the design, it's just there.
Should not have
• I don't like a lot of busy-ness or textures
• Also I don't have a logo (not sure where else to specify this)

```html
<!DOCTYPE html>
<html lang="en">
<head>
<meta charset="utf-8">
<title>Delphine Warrow — Independent Cleaner business card</title>
<link href="https://fonts.googleapis.com/css2?family=Open+Sans:wght@400;600;700&display=swap" rel="stylesheet">
<style>
  :root {
    --backdrop: #d6d7d9;
    --paper: #fbfbfa;
    --wash-blue: #5d9fdc;
    --wash-mid: #7fa3dc;
    --wash-lilac: #9a9fd8;
    --name-blue: #8796d4;
    --tagline: #aab4e2;
    --ink: #3a3a3a;
    --icon: #97a5dc;
    --white: #ffffff;
  }
  * { margin: 0; padding: 0; box-sizing: border-box; }
  html, body {
    width: 960px; height: 1200px; overflow: hidden;
    background: var(--backdrop);
    font-family: "Open Sans", Arial, sans-serif;
  }
  .canvas { position: relative; width: 960px; height: 1200px; }
  .card {
    position: absolute; left: 60px; width: 840px; height: 480px;
    background: var(--paper); overflow: hidden;
    box-shadow: 0 10px 28px rgba(0,0,0,0.18);
  }
  .card--back { top: 90px; }
  .card--front { top: 630px; }
  .wash { position: absolute; inset: 0; width: 100%; height: 100%; }

  /* back */
  .back-brand {
    position: absolute; left: 0; right: 0; top: 150px; text-align: center;
    color: var(--white);
  }
  .back-brand__name { font-size: 92px; font-weight: 600; letter-spacing: 1px; line-height: 1; }
  .back-brand__role { margin-top: 18px; font-size: 34px; font-weight: 400; letter-spacing: 2px; opacity: 0.92; }

  /* front */
  .initials {
    position: absolute; left: 120px; top: 60px;
    font-size: 96px; font-weight: 600; color: var(--white); letter-spacing: 2px;
  }
  .contact { position: absolute; right: 36px; top: 100px; text-align: right; }
  .contact__name { font-size: 36px; font-weight: 700; color: var(--name-blue); line-height: 1.1; margin-right: 48px; }
  .contact__role { font-size: 23px; color: var(--ink); margin-right: 48px; }
  .contact__line {
    display: flex; align-items: center; justify-content: flex-end; gap: 14px;
    font-size: 25px; color: var(--ink); margin-top: 8px;
  }
  .contact__line--first { margin-top: 44px; }
  .contact__icon { width: 34px; height: 34px; flex: none; }
  .tagline {
    position: absolute; left: 36px; bottom: 34px;
    font-size: 44px; font-weight: 600; color: var(--tagline); letter-spacing: 1px;
  }
</style>
</head>
<body>
<div class="canvas">

  <section class="card card--back" aria-label="Card back">
    <svg class="wash" viewBox="0 0 840 480" role="img" aria-label="Soft blue watercolour wash covering most of the card">
      <defs>
        <linearGradient id="washBack" x1="0" y1="0" x2="1" y2="1">
          <stop offset="0" stop-color="#5d9fdc"/>
          <stop offset="0.55" stop-color="#7fa3dc"/>
          <stop offset="1" stop-color="#9a9fd8"/>
        </linearGradient>
      </defs>
      <path fill="url(#washBack)" d="M40 40 L120 18 L300 30 L520 12 L700 26 L810 40 L828 120 L820 260 L832 400 L780 452 L600 440 L420 456 L240 430 L90 440 L30 380 L18 240 L30 120 Z"/>
    </svg>
    <div class="back-brand">
      <div class="back-brand__name">Warrow</div>
      <div class="back-brand__role">Independent Cleaner</div>
    </div>
  </section>

  <section class="card card--front" aria-label="Card front">
    <svg class="wash" viewBox="0 0 840 480" role="img" aria-label="Soft blue watercolour wash in the upper left corner">
      <defs>
        <linearGradient id="washFront" x1="0" y1="0" x2="1" y2="1">
          <stop offset="0" stop-color="#5d9fdc"/>
          <stop offset="0.6" stop-color="#7fa3dc"/>
          <stop offset="1" stop-color="#9a9fd8"/>
        </linearGradient>
      </defs>
      <path fill="url(#washFront)" d="M0 0 L420 0 L436 60 L428 130 L402 176 L388 230 L350 262 L300 270 L250 300 L180 316 L90 330 L0 338 Z"/>
    </svg>
    <div class="initials">DW</div>
    <div class="contact">
      <div class="contact__name">Delphine Warrow</div>
      <div class="contact__role">Independent Cleaner</div>
      <div class="contact__line contact__line--first">
        <span>604-317-2269</span>
        <svg class="contact__icon" viewBox="0 0 34 34" aria-hidden="true">
          <circle cx="17" cy="17" r="17" fill="var(--icon)"/>
          <path d="M12 9 l3 0 l1.5 4 l-2 1.5 a10 10 0 0 0 5 5 l1.5 -2 l4 1.5 l0 3 a2 2 0 0 1 -2 2 a14 14 0 0 1 -13 -13 a2 2 0 0 1 2 -2 z" fill="#fff"/>
        </svg>
      </div>
      <div class="contact__line">
        <span>mtb.warrow@postmail.example</span>
        <svg class="contact__icon" viewBox="0 0 34 34" aria-hidden="true">
          <circle cx="17" cy="17" r="17" fill="var(--icon)"/>
          <rect x="9" y="11" width="16" height="12" rx="1" fill="#fff"/>
          <path d="M9 12 L17 18 L25 12" fill="none" stroke="var(--icon)" stroke-width="1.6"/>
        </svg>
      </div>
    </div>
    <div class="tagline">RELIABLE • CUSTOM • THOROUGH</div>
  </section>

</div>
</body>
</html>
```